Corvanta512 Business Card Redesign

I want to create a design for brand new business cards, I need something exceptional for clear plastic business card design. Please do not submit without it being on a clear design. Photos of the various logo versions attached.

```html
<!DOCTYPE html>
<html lang="en">
<head>
<meta charset="utf-8">
<title>Corvanta512 Business Card</title>
<link href="https://fonts.googleapis.com/css2?family=Poppins:wght@400;500;600&display=swap" rel="stylesheet">
<style>
  :root {
    --page-bg: #dfe4ea;
    --card-clear: #f3f5f8;
    --card-edge: rgba(255,255,255,0.9);
    --navy: #2c3350;
    --navy-deep: #1d2133;
    --gold: #a98a45;
    --text-dark: #2f3034;
    --icon-grey: #6e6f74;
  }
  * { margin: 0; padding: 0; box-sizing: border-box; }
  html, body {
    width: 1200px; height: 900px; overflow: hidden;
    background: var(--page-bg);
    font-family: "Poppins", sans-serif;
  }
  .business-card {
    position: absolute; left: 80px; top: 154px;
    width: 1040px; height: 592px;
    background: linear-gradient(160deg, rgba(255,255,255,0.92), var(--card-clear) 60%, #e8ecf1);
    border: 1px solid var(--card-edge);
    box-shadow: 0 12px 40px rgba(40,50,70,0.18);
    overflow: hidden;
  }
  .corner-band { position: absolute; right: 0; bottom: 0; width: 1040px; height: 592px; }
  .contact-block { position: absolute; left: 70px; top: 178px; color: var(--text-dark); }
  .person-name { font-size: 37px; font-weight: 600; color: var(--navy); line-height: 1.1; letter-spacing: 0.3px; }
  .person-role { font-size: 21px; font-weight: 400; letter-spacing: 0.8px; margin-top: 2px; margin-left: 3px; }
  .address { margin-top: 30px; font-size: 20.5px; line-height: 27px; }
  .contact-list { list-style: none; margin-top: 30px; font-size: 21px; }
  .contact-list li { display: flex; align-items: center; height: 29px; }
  .contact-list svg { width: 18px; height: 18px; margin-right: 24px; margin-left: 3px; fill: var(--icon-grey); }
  .brand-lockup {
    position: absolute; left: 520px; top: 300px;
    display: flex; align-items: center; gap: 16px;
  }
  .brand-dot { width: 26px; height: 26px; border-radius: 50%; background: var(--gold); }
  .brand-name { font-size: 52px; font-weight: 600; color: var(--gold); letter-spacing: 1px; }
</style>
</head>
<body>
  <section class="business-card">
    <svg class="corner-band" viewBox="0 0 1040 592" aria-hidden="true">
      <path d="M714 592 C860 540 990 430 1040 322 L1040 592 Z" fill="var(--navy-deep)"/>
    </svg>

    <div class="contact-block">
      <h1 class="person-name">Dale Fenwick</h1>
      <p class="person-role">Sales &amp; Estimating</p>
      <p class="address">48 Harlow Ave Suite 1204<br>Bramwell, PA 19370</p>
      <ul class="contact-list">
        <li>
          <svg viewBox="0 0 20 20" aria-hidden="true"><path d="M2 7c0-2 3-4 8-4s8 2 8 4v2h-4V7.5c-1-.6-2.3-.9-4-.9s-3 .3-4 .9V9H2z M4 11h12l1 6H3z"/></svg>
          (555) 214-6093
        </li>
        <li>
          <svg viewBox="0 0 20 20" aria-hidden="true"><path d="M2 5h16v10H2z M2 5l8 6 8-6" stroke="#f3f5f8" stroke-width="1.2"/></svg>
          info@corvanta512.com
        </li>
        <li>
          <svg viewBox="0 0 20 20" aria-hidden="true"><circle cx="10" cy="10" r="8"/><path d="M5 6c2 0 3 2 2 4s1 3 0 5M13 4c-1 2 1 3 3 3" stroke="#f3f5f8" stroke-width="1.4" fill="none"/></svg>
          www.corvanta512.com
        </li>
      </ul>
    </div>

    <div class="brand-lockup">
      <span class="brand-dot"></span>
      <span class="brand-name">Corvanta512</span>
    </div>
  </section>
</body>
</html>
```